Landing page for Cloud Kitchen buisnies

We need a landing page design fully functional for our Cloud Kitchen company wich is based in Dubai we have a industrial kitchen setup up from where we operate our own online food brands wich are only availble for delivery

Target Market(s)

Its just a company Profile

Requirements
Must have
• Company name is Saffron Lane Group. We have the Logo already

LOGO AND DOMAIN WE HAVE
Nice to have
• Proffesionel high quality design

```html
<!DOCTYPE html>
<html lang="en">
<head>
<meta charset="utf-8">
<title>Saffron Lane Group — Cloud Kitchen</title>
<link href="https://fonts.googleapis.com/css2?family=Roboto:wght@400;500;700&family=IBM+Plex+Sans:ital,wght@0,400;0,500;1,400&display=swap" rel="stylesheet">
<style>
  :root {
    --gold: #c9a13a;
    --gold-light: #e6c65f;
    --gold-dark: #b0841f;
    --white: #ffffff;
    --text-soft: #e9e9e9;
    --bg-about: #0b0b0d;
    --bg-partners: #0d0d0f;
    --bg-footer: #060607;
    --partner-grey: #5c5c60;
  }
  * { margin: 0; padding: 0; box-sizing: border-box; }
  html, body { width: 858px; height: 1200px; overflow: hidden; background: var(--bg-footer); }
  body { position: relative; font-family: "IBM Plex Sans", Arial, sans-serif; color: var(--white); }

  .hero { position: absolute; left: 0; top: 0; width: 858px; height: 481px; overflow: hidden; }
  .hero-photo {
    position: absolute; inset: 0;
    background:
      radial-gradient(ellipse 230px 200px at 120px 250px, rgba(232,120,30,.85), rgba(190,70,20,.35) 55%, transparent 80%),
      radial-gradient(ellipse 260px 160px at 560px 360px, rgba(120,110,110,.45), transparent 75%),
      radial-gradient(ellipse 330px 90px at 650px 440px, rgba(120,60,30,.6), transparent 80%),
      linear-gradient(180deg, #2a2c3a 0%, #3b3a48 40%, #2a2324 75%, #121010 100%);
  }
  .contact { position: absolute; left: 67px; top: 13px; display: flex; align-items: center; gap: 7px; }
  .contact-icon { width: 33px; height: 33px; border-radius: 50%; border: 1.5px solid var(--gold); display: flex; align-items: center; justify-content: center; }
  .contact-label { font-family: "Roboto", sans-serif; font-size: 11px; line-height: 13px; }
  .contact-number { font-family: "Roboto", sans-serif; font-weight: 700; font-size: 17px; line-height: 20px; letter-spacing: .3px; }

  .auth { position: absolute; top: 16px; left: 604px; display: flex; gap: 8px; }
  .btn { height: 28px; width: 88px; border-radius: 14px; font-family: "Roboto", sans-serif; font-weight: 500; font-size: 12px; display: flex; align-items: center; justify-content: center; color: var(--white); }
  .btn-gold { background: linear-gradient(180deg, var(--gold-light), var(--gold-dark)); }
  .btn-outline { border: 1.5px solid var(--white); }

  .brand { position: absolute; top: 100px; left: 0; width: 858px; text-align: center; font-family: "Roboto", sans-serif; color: var(--gold); font-weight: 500; }
  .brand-name { font-size: 22px; letter-spacing: 2px; }
  .brand-sub { font-size: 12px; letter-spacing: 6px; margin-top: 2px; }

  .hero-box { position: absolute; left: 216px; top: 214px; width: 426px; height: 122px; border: 3px solid var(--gold); text-align: center; }
  .hero-title { font-family: "Roboto", sans-serif; font-weight: 700; font-size: 29px; margin-top: 17px; line-height: 34px; }
  .hero-text { font-family: "Roboto", sans-serif; font-size: 15px; line-height: 22px; margin-top: 3px; }
  .order-btn { position: absolute; left: 380px; top: 320px; width: 98px; height: 28px; }

  .about { position: absolute; left: 0; top: 481px; width: 858px; height: 499px; }
  .about-photo { position: absolute; inset: 0; background: radial-gradient(ellipse 500px 260px at 430px 320px, #1a1a1d, var(--bg-about) 80%); }
  .about-mark { position: absolute; left: 413px; top: 48px; width: 32px; height: 32px; border: 1.5px solid var(--white); border-radius: 50%; }
  .about-title { position: absolute; top: 84px; width: 858px; text-align: center; font-family: "Roboto", sans-serif; font-weight: 700; font-size: 23px; }
  .about-text { position: absolute; top: 117px; left: 110px; width: 638px; text-align: center; font-style: italic; font-size: 12px; line-height: 22px; color: var(--text-soft); }

  .step { position: absolute; width: 200px; text-align: center; }
  .step-circle { position: relative; width: 81px; height: 81px; margin: 0 auto; border: 1.5px solid var(--gold); border-radius: 50%; display: flex; align-items: center; justify-content: center; }
  .step-badge { position: absolute; left: 1px; top: 3px; width: 20px; height: 20px; border-radius: 50%; background: var(--gold); font-size: 11px; font-weight: 500; display: flex; align-items: center; justify-content: center; }
  .step-title { font-family: "Roboto", sans-serif; font-weight: 500; font-size: 15.5px; line-height: 22px; margin-top: 11px; }
  .step-text { font-size: 11.5px; line-height: 18px; margin-top: 2px; color: var(--text-soft); }
  .step-1 { left: 58px; top: 228px; }
  .step-2 { left: 322px; top: 279px; }
  .step-3 { left: 586px; top: 228px; }
  .step-flow { position: absolute; left: 0; top: 0; }

  .partners { position: absolute; left: 0; top: 980px; width: 858px; height: 148px; background: var(--bg-partners); }
  .partner { position: absolute; top: 60px; display: flex; align-items: center; gap: 8px; font-family: "IBM Plex Sans", sans-serif; font-weight: 500; font-size: 20px; color: var(--partner-grey); transform: translateX(-50%); white-space: nowrap; }
  .partner-dot { width: 22px; height: 22px; border-radius: 50%; background: var(--partner-grey); }

  .footer { position: absolute; left: 0; top: 1128px; width: 858px; height: 72px; background: var(--bg-footer); }
  .footer-copy { position: absolute; left: 72px; top: 25px; font-size: 10px; color: var(--text-soft); }
  .social { position: absolute; left: 691px; top: 22px; display: flex; gap: 6px; }
  .social-link { width: 27px; height: 27px; border: 1.5px solid var(--gold); border-radius: 50%; }
</style>
</head>
<body>
  <header class="hero">
    <div class="hero-photo" role="img" aria-label="Photo of a chef cooking over a flaming wok in an industrial kitchen"></div>

    <div class="contact">
      <div class="contact-icon">
        <svg width="14" height="14" viewBox="0 0 24 24" fill="none" stroke="#fff" stroke-width="2" stroke-linecap="round" stroke-linejoin="round"><path d="M22 16.9v3a2 2 0 0 1-2.2 2 19.8 19.8 0 0 1-8.6-3.1 19.5 19.5 0 0 1-6-6A19.8 19.8 0 0 1 2.1 4.2 2 2 0 0 1 4.1 2h3a2 2 0 0 1 2 1.7c.1 1 .4 1.9.7 2.8a2 2 0 0 1-.5 2.1L8 9.9a16 16 0 0 0 6 6l1.3-1.3a2 2 0 0 1 2.1-.5c.9.3 1.8.6 2.8.7a2 2 0 0 1 1.8 2.1z"/></svg>
      </div>
      <div>
        <div class="contact-label">Call For Order</div>
        <div class="contact-number">555 014 2270</div>
      </div>
    </div>

    <div class="brand">
      <div class="brand-name">SAFFRON LANE</div>
      <div class="brand-sub">GROUP</div>
    </div>

    <nav class="auth">
      <a class="btn btn-gold">SIGN UP</a>
      <a class="btn btn-outline">LOGIN</a>
    </nav>

    <section class="hero-box">
      <h1 class="hero-title">CLOUD KITCHEN</h1>
      <p class="hero-text">we operate our own online food brands<br>wich are only availble for delivery</p>
    </section>
    <a class="btn btn-gold order-btn">ORDER NOW</a>
  </header>

  <section class="about">
    <div class="about-photo" role="img" aria-label="Dark photo of a commercial kitchen"></div>
    <div class="about-mark"></div>
    <h2 class="about-title">ABOUT SAFFRON LANE GROUP</h2>
    <p class="about-text">Lorem ipsum dolor sit amet, consectetur adipiscing elit, sed do eiusmod tempor incididunt ut labore et dolore magna aliqua. Quis ipsum suspendisse ultrices gravida. Risus commodo viverra maecenas Lorem ipsum dolor sit amet, consectetur adipiscing elit, sed do eiusmod tempor incididunt ut labore et dolore magna aliqua.</p>

    <svg class="step-flow" width="858" height="499" viewBox="0 0 858 499" fill="none" stroke="#a8842e" stroke-width="2.5" stroke-linecap="round">
      <path d="M213 272 C 240 295, 330 280, 360 300" stroke-dasharray="3 5"/>
      <path d="M354 295 L362 301 L352 302" stroke-dasharray="none" stroke-width="2"/>
      <path d="M484 308 C 540 320, 560 250, 625 263" stroke-dasharray="3 5"/>
      <path d="M618 258 L627 263 L619 268" stroke-width="2"/>
    </svg>

    <div class="step step-1">
      <div class="step-circle">
        <span class="step-badge">1</span>
        <svg width="36" height="32" viewBox="0 0 36 32" fill="none" stroke="#d8b04a" stroke-width="2"><circle cx="8" cy="6" r="4"/><circle cx="18" cy="6" r="4"/><circle cx="28" cy="6" r="4"/><path d="M2 30V18a5 5 0 0 1 5-5h22a5 5 0 0 1 5 5v12M12 30V19M24 30V19"/></svg>
      </div>
      <h3 class="step-title">You Join a group</h3>
      <p class="step-text">Lorem ipsum dolor et, consectetur<br>adipiscing elit, sed do</p>
    </div>

    <div class="step step-2">
      <div class="step-circle">
        <span class="step-badge">2</span>
        <svg width="34" height="32" viewBox="0 0 34 32" fill="none" stroke="#d8b04a" stroke-width="2"><rect x="2" y="2" width="30" height="21" rx="2"/><path d="M12 30h10M17 23v7M2 8h30M7 18h8M20 13h8M20 18h6"/></svg>
      </div>
      <h3 class="step-title">You Place Your Order<br>With The Rest of The Group</h3>
      <p class="step-text">Lorem ipsum dolor et, consectetur<br>adipiscing elit, sed do</p>
    </div>

    <div class="step step-3">
      <div class="step-circle">
        <span class="step-badge">3</span>
        <svg width="34" height="34" viewBox="0 0 34 34" fill="none" stroke="#d8b04a" stroke-width="2"><path d="M10 8V4h10v4"/><rect x="4" y="8" width="22" height="24" rx="2"/><path d="M9 16h2M14 16h6M9 22h2M14 22h6M9 27h2"/><circle cx="27" cy="24" r="5"/></svg>
      </div>
      <h3 class="step-title">The Foods Get Delivered<br>To The Group</h3>
      <p class="step-text">Lorem ipsum dolor et, consectetur<br>adipiscing elit, sed do</p>
    </div>
  </section>

  <section class="partners">
    <div class="partner" style="left:172px">Ember Plate</div>
    <div class="partner" style="left:348px"><span class="partner-dot"></span>Olive Row</div>
    <div class="partner" style="left:522px"><span class="partner-dot"></span>Bakewell</div>
    <div class="partner" style="left:680px"><span class="partner-dot"></span>Tidewell</div>
  </section>

  <footer class="footer">
    <p class="footer-copy">Saffron Lane Group. © 2020 All Rights Reserved | Privacy Policy</p>
    <div class="social">
      <a class="social-link" aria-label="Social profile 1"></a>
      <a class="social-link" aria-label="Social profile 2"></a>
      <a class="social-link" aria-label="Social profile 3"></a>
    </div>
  </footer>
</body>
</html>
```